New Business Card Design Project

2 sided business card required. I have attached some previous designs of items we have had made so you can see the logo etc. we Want the card to look professional and modern. for the final design upload for winning designer please note I need to be able to edit the names / phone numbers on the card design as I need to get them made for different staff.
Updates

extending time so designers can have time to submit

Target Market(s)

new customers

Industry/Entity Type

transport / earthmoving

Contact Information for Business Card

name, phone number email address

Requirements
Nice to have
• professional / impressive looking card (first impressions to customers count)
Should not have
• do not put our mobile number on the design use a generic number

```html
<!DOCTYPE html>
<html lang="en">
<head>
<meta charset="utf-8">
<title>RDX Pty Ltd – Business Card</title>
<link rel="stylesheet" href="https://fonts.googleapis.com/css2?family=Oswald:wght@500;700&family=Tinos:wght@700&display=swap">
<style>
  :root {
    --page-bg: #2b2b2d;
    --card-black: #070707;
    --panel-dark: #1a1c1b;
    --steel-dark: #151515;
    --steel-mid: #3a3732;
    --steel-light: #6b665e;
    --accent-orange: #d99a55;
    --text-white: #f4f4f4;
    --logo-silver: #c9c9c9;
  }
  * { margin: 0; padding: 0; box-sizing: border-box; }
  html, body {
    width: 1200px; height: 1200px; overflow: hidden;
    background: var(--page-bg);
  }
  .canvas { position: relative; width: 1200px; height: 1200px; }
  .card {
    position: absolute; left: 150px; width: 900px; height: 514px;
    background: var(--card-black); overflow: hidden;
  }
  .card--front { top: 44px; }
  .card--back { top: 642px; }
  .card > svg { position: absolute; inset: 0; }

  .brand {
    position: absolute;
    font-family: "Oswald", sans-serif; font-weight: 700;
    color: var(--logo-silver); letter-spacing: 4px;
    display: flex; align-items: center; gap: 14px;
  }
  .brand__mark { width: 18px; height: 18px; background: var(--logo-silver); }
  .card--front .brand { left: 470px; top: 110px; font-size: 92px; line-height: 1; }
  .card--back .brand { left: 560px; top: 196px; font-size: 64px; line-height: 1; }
  .brand small { font-size: 0.32em; letter-spacing: 2px; align-self: flex-end; margin-bottom: 10px; }

  .contact {
    position: absolute; display: flex; align-items: center; gap: 18px;
    font-family: "Tinos", serif; font-weight: 700; color: var(--text-white);
  }
  .card--front .contact { left: 300px; top: 300px; font-size: 38px; letter-spacing: 2px; }

  .person { position: absolute; left: 60px; top: 28px; }
  .person__name {
    font-family: "Oswald", sans-serif; font-weight: 700; font-size: 50px;
    color: var(--accent-orange); letter-spacing: 1px; margin-left: 62px; line-height: 1.1;
  }
  .person .contact { position: relative; font-size: 24px; gap: 14px; margin-top: 4px; }

  .services-title {
    position: absolute; left: 44px; top: 226px;
    font-family: "Oswald", sans-serif; font-weight: 700; font-size: 32px; line-height: 1.2;
    color: var(--text-white); letter-spacing: 1px;
  }
  .service-list {
    position: absolute; list-style: none;
    font-family: "Oswald", sans-serif; font-weight: 500; font-size: 17px;
    color: var(--accent-orange); line-height: 1.45; text-transform: uppercase;
  }
  .service-list li { display: flex; align-items: flex-start; gap: 12px; }
  .service-list li::before {
    content: ""; width: 13px; height: 13px; margin-top: 6px;
    background: var(--text-white); flex: none;
  }
  .service-list--first { left: 30px; top: 276px; }
  .service-list--second { left: 300px; top: 332px; }
  .service-list--third { left: 600px; top: 398px; width: 230px; font-size: 16px; }
  .service-list--third li::before { margin-top: 5px; }
</style>
</head>
<body>
<main class="canvas">

  <section class="card card--front" aria-label="Business card front">
    <svg width="900" height="514" viewBox="0 0 900 514">
      <defs>
        <radialGradient id="front-photo" cx="0.55" cy="0.35" r="0.7">
          <stop offset="0" stop-color="var(--steel-light)"/>
          <stop offset="0.45" stop-color="var(--steel-mid)"/>
          <stop offset="1" stop-color="var(--steel-dark)"/>
        </radialGradient>
      </defs>
      <rect class="front-photo" width="900" height="514" fill="url(#front-photo)"
            role="img" aria-label="Road train trucks on a dark perforated metal background"/>
    </svg>
    <div class="brand"><span class="brand__mark"></span>RDX <small>Pty Ltd</small></div>
    <div class="contact">
      <svg width="34" height="24" viewBox="0 0 34 24" aria-hidden="true">
        <rect x="1" y="1" width="32" height="22" fill="var(--text-white)"/>
        <path d="M1 1 L17 13 L33 1" fill="none" stroke="var(--card-black)" stroke-width="2"/>
      </svg>
      xyz@haulmail.com
    </div>
  </section>

  <section class="card card--back" aria-label="Business card back">
    <svg width="900" height="514" viewBox="0 0 900 514">
      <defs>
        <radialGradient id="back-photo" cx="0.7" cy="0.3" r="0.55">
          <stop offset="0" stop-color="var(--steel-light)"/>
          <stop offset="0.5" stop-color="var(--steel-mid)"/>
          <stop offset="1" stop-color="var(--steel-dark)"/>
        </radialGradient>
        <linearGradient id="services-panel" x1="0" y1="0" x2="1" y2="1">
          <stop offset="0" stop-color="#262927"/>
          <stop offset="1" stop-color="var(--card-black)"/>
        </linearGradient>
      </defs>
      <polygon class="services-panel" points="0,212 580,174 900,150 900,514 0,514" fill="url(#services-panel)"/>
      <polygon class="back-photo" points="260,228 580,172 900,150 900,400" fill="url(#back-photo)"
               role="img" aria-label="Road train trucks on a dark perforated metal background"/>
      <polygon class="divider-band" points="0,198 580,166 580,174 0,214" fill="var(--text-white)"/>
      <line class="divider-line" x1="260" y1="228" x2="580" y2="170" stroke="var(--text-white)" stroke-width="5"/>
      <line class="divider-line" x1="260" y1="228" x2="900" y2="400" stroke="var(--text-white)" stroke-width="6"/>
    </svg>

    <div class="person">
      <div class="person__name">JOHN DOE</div>
      <div class="contact">
        <svg width="22" height="22" viewBox="0 0 24 24" aria-hidden="true">
          <path d="M6.6 10.8a15 15 0 0 0 6.6 6.6l2.2-2.2a1 1 0 0 1 1-.25 11.4 11.4 0 0 0 3.6.6 1 1 0 0 1 1 1V20a1 1 0 0 1-1 1A17 17 0 0 1 3 4a1 1 0 0 1 1-1h3.5a1 1 0 0 1 1 1 11.4 11.4 0 0 0 .6 3.6 1 1 0 0 1-.25 1z" fill="var(--text-white)"/>
        </svg>
        <span>1234567890</span>
      </div>
      <div class="contact">
        <svg width="24" height="17" viewBox="0 0 34 24" aria-hidden="true">
          <rect x="1" y="1" width="32" height="22" fill="var(--text-white)"/>
          <path d="M1 1 L17 13 L33 1" fill="none" stroke="var(--card-black)" stroke-width="2"/>
        </svg>
        <span>xyz@haulmail.com</span>
      </div>
    </div>

    <div class="brand"><span class="brand__mark"></span>RDX <small>Pty Ltd</small></div>

    <h2 class="services-title">OUR SERVICES</h2>
    <ul class="service-list service-list--first">
      <li>Over size loads | Hot shot loads</li>
      <li>Heavy vehicle recovery services</li>
      <li>Potable water deliveries</li>
      <li>Road building / maintenance</li>
    </ul>
    <ul class="service-list service-list--second">
      <li>Sand metal supply &amp; cartage</li>
      <li>Road train tippers</li>
      <li>Road train tankers</li>
      <li>Road train flat tops</li>
    </ul>
    <ul class="service-list service-list--third">
      <li>Drop deck trailers</li>
      <li>Mine site accredited equipment &amp; operators</li>
      <li>Earthworks</li>
    </ul>
  </section>

</main>
</body>
</html>
```